Book Cover on Entrepreneurship for Eye Doctors

Book Title: The Lens Clinic Founder: How to begin with steady footing
Author: Rupert Malveski, Optom, MBA, DBA, EIC
I need a Book Cover with the following descriptions:
Topic: the book topic is entrepreneurship knowledge for eye care professionals.
The book's audience: eye care professionals who you know as Opticians, who sell eyeglasses and sunglasses;
Optometrists, test eyes, fit contact lenses, and prescribe medication
Ophthalmologists, perform eye surgery
More about the audience:
1- Young eye care professionals who don’t know about entrepreneurship and those who are stuck in the 9-to-5 job;
2- This is the first book written on entrepreneurship with eye care professionals in mind.
3- Private practice owners the established business guys who are looking to grow their business;
4- Many eye care professionals are MBA holders they may have learned a little bit about entrepreneurship during their MBA studies.
Use the sample cover above and the suggestions that follow as a guide:
1- The cover should be very simple leaving an empty space somewhere to sign the book;
2- The Title and author name should use a modern font;
3- The cover should provide info about what's inside the book through illustrations, for example:
a- Gears: illustrating entrepreneur growth mindset (or anything more explicit)
b- Spectacles, sunglasses, lenses, eye drops, or any other eye care-related correction tools illustrating eye care (or anything more explicit)
c- Symbols illustrating ideas, opportunity, and profit, like money, charts, light bulbs, brain, and coins,...(or anything more explicit)
d- Entrepreneurship illustrated by Briefcase, tie, suit,... (or anything more explicit)

The rest is your creativity and imagination interplay.

Target Market(s)

Eye care professionals: Opticians, Optometrists, Ophthalmologists, Eye Care Administrators, Students in eye specialties.

Industry/Entity Type

eye care

Requirements
Must have
• 1- The cover should be very simple leaving an empty space somewhere to sign the book; 2- The Title and author name should use a modern font; 3- The cover should provide info about what's inside the book through illustrations, for example: a- Gears: illustrating entrepreneur growth mindset (or anything more explicit) b- Spectacles, sunglasses, lenses, eye drops, or any other eye care-related correction tools illustrating eye care (or anything more explicit) c- Symbols illustrating ideas, opportunity, and profit, like money, charts, light bulbs, brain, and coins,...(or anything more explicit) d- Entrepreneurship illustrated by Briefcase, tie, suit,... (or anything more explicit)

```html
<!DOCTYPE html>
<html lang="en">
<head>
<meta charset="utf-8">
<title>The Lens Clinic Founder – Book Cover Wrap</title>
<link rel="stylesheet" href="https://fonts.googleapis.com/css2?family=Bebas+Neue&family=Montserrat:wght@400;700&display=swap">
<style>
  :root {
    --navy: #0b2340;
    --cyan: #0ea8cc;
    --paper: #e6f3f4;
    --ink: #16253a;
    --white: #ffffff;
    --photo-top: #1e3d60;
    --photo-mid: #4a7ea3;
    --photo-low: #bfe0e8;
  }
  html, body {
    margin: 0;
    padding: 0;
    width: 1200px;
    height: 831px;
    overflow: hidden;
    background: var(--paper);
  }
  .cover-wrap {
    position: relative;
    width: 1200px;
    height: 831px;
    background: var(--paper);
    overflow: hidden;
    font-family: "Montserrat", sans-serif;
    color: var(--ink);
  }
  .display {
    font-family: "Bebas Neue", sans-serif;
  }
  /* Bottom band */
  .base-band {
    position: absolute;
    left: 0; top: 760px;
    width: 1200px; height: 71px;
    background: var(--navy);
  }
  .base-band .fold {
    position: absolute;
    left: 553px; top: 0;
    width: 1px; height: 71px;
    background: rgba(255,255,255,0.12);
  }
  .fold-line {
    position: absolute;
    left: 646px; top: 0;
    width: 1px; height: 760px;
    background: rgba(11,35,64,0.06);
  }
  /* Front */
  .front-art {
    position: absolute;
    left: 646px; top: 0;
    width: 554px; height: 330px;
    background:
      radial-gradient(ellipse at 55% 70%, rgba(240,170,130,0.55), rgba(240,170,130,0) 45%),
      radial-gradient(ellipse at 80% 55%, rgba(60,210,220,0.5), rgba(60,210,220,0) 40%),
      linear-gradient(180deg, var(--photo-top) 0%, var(--photo-mid) 55%, var(--photo-low) 85%, var(--paper) 100%);
  }
  .front-title, .front-author, .spine-type, .back-title, .back-author {
    position: absolute;
    overflow: visible;
  }
  .front-title { left: 0; top: 0; width: 1200px; height: 760px; }
  .front-author { left: 0; top: 760px; width: 1200px; height: 71px; }
  .spine-type { left: 0; top: 0; width: 1200px; height: 760px; }
  .back-title { left: 206px; top: 29px; width: 142px; height: 107px; }
  .back-author { left: 120px; top: 463px; width: 312px; height: 24px; }
  /* Back */
  .back-blurb {
    position: absolute;
    left: 30px; top: 144px;
    width: 494px;
    font-size: 9.9px;
    line-height: 12.3px;
    text-align: justify;
  }
  .back-blurb p { margin: 0 0 4.5px; }
  .author-portrait {
    position: absolute;
    left: 30px; top: 500px;
    width: 149px; height: 204px;
    background: linear-gradient(180deg, #d6d3d6 0%, #c7c2c5 55%, #3a4250 80%, #2b3140 100%);
  }
  .author-bio {
    position: absolute;
    left: 185px; top: 496px;
    width: 339px;
    margin: 0;
    font-size: 9.9px;
    line-height: 12.3px;
    text-align: justify;
  }
  .author-bio strong { font-weight: 700; color: var(--navy); }
</style>
</head>
<body>
<div class="cover-wrap">

  <!-- Back cover -->
  <svg class="back-title display" viewBox="0 0 142 107" aria-label="The Lens Clinic Founder">
    <text x="0" y="39" font-size="56" fill="var(--navy)" textLength="142" lengthAdjust="spacingAndGlyphs">THE LENS</text>
    <text x="0" y="81" font-size="55" fill="var(--navy)" textLength="142" lengthAdjust="spacingAndGlyphs">CLINIC</text>
    <text x="0" y="106" font-size="29" fill="var(--cyan)" textLength="142" lengthAdjust="spacingAndGlyphs">FOUNDER</text>
  </svg>

  <div class="back-blurb">
    <p>Before you decide to enroll in a Master of Business Administration (MBA) program read this book.</p>
    <p>Ophthalmologists, Optometrists, and every eye care professional are lifelong learners. At a certain point during their career they find themselves in need of more business knowledge. Most of them resume their development through completing a Master of Business Administration (MBA) degree or another business degree. I argue that learning entrepreneurship is better than pursuing an MBA. Now I wrote this timely book to provide the basic knowledge that every eye care professional needs to know about entrepreneurship.</p>
    <p>This book does not prepare eye care professionals to work in or on the administrative process, or bring a professional opinion in their department within the practice. Moreover, it does not prepare them to go out of the clinical part of the practice or make a transition to management the way an MBA does. Instead, this book helps them see the “Opportunity” that they are after. It helps them focus on what is best no matter how ambiguous the environment is or the situation they are facing. I argue that an MBA may be useful, however in a rapidly changing world and in the face of uncertainty, an MBA takes long enough time to miss the opportunity they are after as professional learners. In this rapidly changing world I emphasize the importance of developing their entrepreneurial spirit which is somehow different than studying an MBA. All the jobs an MBA will enable the eye care professional to do can be performed by a practice manager or simply outsourced. However, no one can outsource identifying and discovering an entrepreneurial opportunity.</p>
    <p>In this book you navigate through the mind of the entrepreneur and highlight the importance of the entrepreneurial spirit for eye care professionals. You will also understand what makes great eye care entrepreneurs in terms of risk-taking, innovation, and tolerance of ambiguity and answer what an entrepreneurial opportunity is, how to identify it, and what resources are needed in order to identify and capture its value.</p>
  </div>

  <svg class="back-author display" viewBox="0 0 312 24" aria-label="Rupert Malveski, Optom, MBA, DBA, EIC">
    <text x="0" y="19" font-size="21" fill="var(--navy)" textLength="312" lengthAdjust="spacing">RUPERT MALVESKI, OPTOM, MBA, DBA, EIC</text>
  </svg>

  <div class="author-portrait" role="img" aria-label="Portrait photograph of the author in a dark suit and tie"></div>

  <p class="author-bio"><strong>Doctor Rupert Malveski</strong> is a serial entrepreneur who is specialized in developing and commercializing eye care products and services using business concepts to solve a variety of eye care practices business problems. To this end, he has extensively worked on crowdsourcing, crowdfunding, disruptive innovation, and cult marketing. He built and helped manage Ophthalmology and Optometry practices as well as many optical shops. He is an Optometrist by trade and studied a Doctorate Degree in Business Administration. He has a long history of more than two decades of working in the retail industry. Besides his strong entrepreneurial knowledge, he has an MBA degree in healthcare management from Harwell Ridge University in Eastvale and a Doctorate degree in Business Administration from Southbrook State University in Millbrook. He is the Editor in Chief at Clearview Optics Journal where he creates and publishes relevant content for helping eye care professionals become better entrepreneurs.</p>

  <!-- Spine -->
  <svg class="spine-type display" viewBox="0 0 1200 760" aria-label="Spine: The Lens Clinic Founder, Rupert Malveski">
    <g transform="translate(612 721) rotate(-90)">
      <text x="0" y="0" font-size="37" textLength="331" lengthAdjust="spacingAndGlyphs"><tspan fill="var(--navy)">THE LENS CLINIC </tspan><tspan fill="var(--cyan)">FOUNDER</tspan></text>
    </g>
    <g transform="translate(608 367) rotate(-90)">
      <text x="0" y="0" font-size="22" fill="var(--navy)" textLength="336" lengthAdjust="spacing">RUPERT MALVESKI, OPTOM, MBA, DBA, EIC</text>
    </g>
  </svg>

  <div class="fold-line"></div>

  <!-- Front cover -->
  <div class="front-art" role="img" aria-label="Photograph of hands with a stylus over glowing business charts, gears, spectacles and an eye icon"></div>

  <svg class="front-title display" viewBox="0 0 1200 760" aria-label="The Lens Clinic Founder: How to begin with steady footing">
    <text x="685" y="461" font-size="178" fill="var(--navy)" textLength="453" lengthAdjust="spacingAndGlyphs">THE LENS</text>
    <text x="685" y="599" font-size="178" fill="var(--navy)" textLength="453" lengthAdjust="spacingAndGlyphs">CLINIC</text>
    <text x="685" y="674" font-size="89" fill="var(--cyan)" textLength="453" lengthAdjust="spacingAndGlyphs">FOUNDER</text>
    <line x1="764" y1="697" x2="1082" y2="697" stroke="var(--cyan)" stroke-width="1.2"/>
    <text x="768" y="725" font-size="28" fill="var(--navy)" textLength="310" lengthAdjust="spacing">HOW TO BEGIN WITH STEADY FOOTING</text>
    <line x1="764" y1="733" x2="1082" y2="733" stroke="var(--cyan)" stroke-width="1.2"/>
  </svg>

  <!-- Base band -->
  <div class="base-band"><div class="fold"></div></div>
  <svg class="front-author display" viewBox="0 0 1200 71" aria-label="Rupert Malveski, Optom, MBA, DBA, EIC">
    <text x="698" y="49" font-size="38" fill="var(--white)" textLength="450" lengthAdjust="spacingAndGlyphs">RUPERT MALVESKI, OPTOM, MBA, DBA, EIC</text>
  </svg>

</div>
</body>
</html>
```